Talbrook Business Card Design

We need to update our current company business cards to something that is more professional. We are oilfield equipment manufacturing company. The company has and will continue to use a logo that is similar to the KORVEN aspirin logo. I would like to see that used alone in the design because that is how most companies recognize us. I also would not mind seeing the logo designed into something more "oilfield" to add some identification to our product line (i.e. maybe a oil rig coming off of it or something). Our units are primarily red, so I would like to stick with a red, black, white, and maybe grey color scheme. In addition to our logo. Our NPQ logo should be on back of card similar to the one I am attaching (FENWICKS). I am in process of getting a clean copy of that image. I am attaching a card (FENWICKS) from a previous company that I worked at that is now closed that I like the design of. I have also attached a current business card.
Updates

I have added our logo and an old business card from a company no longer in existence that I really like the design of. Please use those items in design and a color scheme of red and black. Grey and white can also be incorporated if needed. I need a design that will also translate easily to letterhead, brochures, documents, etc. I plan on also having those designed when I find the right designer.

Industry/Entity Type

Business

Contact Information for Business Card

Front

Talbrook Services (and logo)

Marla Pritchett
Management Rep

361-574-8826 Phone
361-574-8829 Fax
361-430-6658 Mobile
mpritchett@talbrookrigworks.example

Back:
Corpus Christi - Headquarters
4190 Sparrow Ln.
Corpus Christi, TX 78316

Texas - North Dakota - Pennsylvania

www.talbrookrigworks.example

Colors
ec2027
000000
5c5c5c
ffffff

Requirements
Nice to have
• The owners do like cards that have an expensive look to them. They feel that they have achieved that previously with raised ink. That feature or something that separates this card from other would be nice.
Should not have
• This card should not be SUPER modern. This is still an "old school" type owned company. The card should be professional thou.

```html
<!DOCTYPE html>
<html lang="en">
<head>
<meta charset="utf-8">
<title>Talbrook Services – Business Card</title>
<link rel="stylesheet" href="https://fonts.googleapis.com/css2?family=Arimo:wght@700&family=Open+Sans:wght@400;600&display=swap">
<style>
  :root {
    --brand-red: #ec2027;
    --deep-red: #8a0b10;
    --mid-red: #c4121b;
    --navy: #0d1a7a;
    --ink: #222222;
    --white: #ffffff;
    --backdrop: #e6e3df;
  }
  * { margin: 0; padding: 0; box-sizing: border-box; }
  html, body { width: 1200px; height: 494px; overflow: hidden; }
  body {
    background: var(--backdrop);
    font-family: "Open Sans", Arial, sans-serif;
    position: relative;
  }
  .card {
    position: absolute;
    border-radius: 24px;
    overflow: hidden;
  }
  /* Front */
  .card-front {
    left: 36px; top: 30px; width: 552px; height: 318px;
    background: var(--white);
    color: var(--ink);
  }
  .accent-tab {
    position: absolute; left: 0; top: 32px; width: 12px; height: 46px;
    background: linear-gradient(90deg, var(--deep-red), var(--brand-red));
  }
  .person-name {
    position: absolute; left: 36px; top: 36px;
    font-size: 17px; font-weight: 600; color: var(--navy);
  }
  .person-title {
    position: absolute; left: 36px; top: 58px;
    font-size: 14px; color: var(--brand-red);
  }
  .address {
    position: absolute; left: 36px; top: 116px;
    font-size: 14px; line-height: 19px;
  }
  .contacts {
    position: absolute; left: 36px; top: 172px; list-style: none;
    font-size: 14px;
  }
  .contacts li { display: flex; align-items: center; height: 23px; }
  .contacts svg { width: 15px; height: 15px; margin-right: 8px; flex: none; }
  .website-front {
    position: absolute; left: 36px; top: 276px;
    font-size: 15px; font-weight: 600; letter-spacing: 0.6px;
  }
  .mark-front {
    position: absolute; left: 372px; top: 38px; width: 82px; height: 82px;
  }
  .company-front {
    position: absolute; left: 286px; width: 256px; top: 126px; text-align: center;
    font-family: "Arimo", Arial, sans-serif; font-weight: 700;
    font-size: 22px; color: var(--brand-red); white-space: nowrap;
  }
  /* Back */
  .card-back {
    left: 618px; top: 148px; width: 552px; height: 316px;
    background: radial-gradient(ellipse at 50% 38%, var(--mid-red) 0%, #a50e15 45%, var(--deep-red) 100%);
    color: var(--white);
    text-align: center;
  }
  .mark-back {
    position: absolute; left: 228px; top: 36px; width: 96px; height: 96px;
  }
  .company-back {
    position: absolute; left: 0; right: 0; top: 154px;
    font-family: "Arimo", Arial, sans-serif; font-weight: 700;
    font-size: 31px; white-space: nowrap;
  }
  .website-back {
    position: absolute; left: 0; right: 0; top: 238px;
    font-size: 13px; letter-spacing: 2px;
  }
</style>
</head>
<body>

<section class="card card-front" aria-label="Card front">
  <div class="accent-tab"></div>
  <p class="person-name">Your Name</p>
  <p class="person-title">Title</p>
  <p class="address">Street Name, City Name<br>Zip Code-00000</p>
  <ul class="contacts">
    <li>
      <svg viewBox="0 0 16 16" aria-hidden="true"><circle cx="8" cy="8" r="7" fill="none" stroke="#1d3b8f" stroke-width="1.4"/><path d="M5.5 4.5l1.6 0 .6 2-1 .8a5 5 0 0 0 2 2l.8-1 2 .6v1.6c-3.5.3-6.3-2.5-6-6z" fill="#1d3b8f"/></svg>
      361 574 8826
    </li>
    <li>
      <svg viewBox="0 0 16 16" aria-hidden="true"><rect x="4.5" y="1" width="7" height="14" rx="1.5" fill="#1d5fbf"/><rect x="5.8" y="3" width="4.4" height="6" fill="#cfe3ff"/></svg>
      361 430 6658
    </li>
    <li>
      <svg viewBox="0 0 16 16" aria-hidden="true"><rect x="4" y="1.5" width="8" height="5" fill="#1d5fbf"/><rect x="1" y="6" width="14" height="6" rx="1" fill="#2a4f9a"/><rect x="4" y="10" width="8" height="4.5" fill="#dfe8f7"/></svg>
      361 574 8829
    </li>
    <li>
      <svg viewBox="0 0 16 16" aria-hidden="true"><rect x="1" y="3.5" width="14" height="9.5" rx="1" fill="#2a4f9a"/><path d="M1.5 4.5L8 9l6.5-4.5" fill="none" stroke="#fff" stroke-width="1.2"/></svg>
      mpritchett@talbrookrigworks.example
    </li>
  </ul>
  <p class="website-front">www.talbrookrigworks.example</p>
  <svg class="mark-front" viewBox="0 0 82 82" aria-hidden="true"><circle cx="41" cy="41" r="37" fill="none" stroke="var(--brand-red)" stroke-width="4"/></svg>
  <p class="company-front">TALBROOK SERVICES</p>
</section>

<section class="card card-back" aria-label="Card back">
  <svg class="mark-back" viewBox="0 0 96 96" aria-hidden="true"><circle cx="48" cy="48" r="43" fill="none" stroke="var(--white)" stroke-width="4.5"/></svg>
  <p class="company-back">TALBROOK SERVICES</p>
  <p class="website-back">www.talbrookrigworks.example</p>
</section>

</body>
</html>
```